Bref créative
Saltmarsh Restaurant
Truly Island-Made
Simple
#41 Estate Coralind
(at the Harbor Bluff Cottages)
Palmhaven, VI 00999
Saltmarsh_Restaurant@bayvistamail.com
www.saltmarshvi-example.com
* Free Wi-fi
* Special events venue-mediations, meetings, fund raisers, wedding receptions, catering, private parties, you name it we can host it !!
* Superior customer service
* Delicious cuisine
please use this logo

```html
<!DOCTYPE html>
<html lang="en">
<head>
<meta charset="utf-8">
<title>Saltmarsh Restaurant — Stationery Set</title>
<link href="https://fonts.googleapis.com/css2?family=Cormorant+Garamond:wght@500&family=Open+Sans:wght@400;600&display=swap" rel="stylesheet">
<style>
:root{
  --stage:#e9e9e9;
  --paper:#ffffff;
  --ink:#333333;
  --muted:#777777;
  --rule:#9a9a9a;
  --brand:#8aa89a;
  --teal:#cfe6e6;
  --teal-deep:#a9d3d3;
  --gold:#c9a45c;
  --night:#111111;
  --shadow:0 1px 3px rgba(0,0,0,.25);
}
*{box-sizing:border-box;margin:0;padding:0}
html,body{width:1200px;height:552px;overflow:hidden;background:var(--stage);font-family:"Open Sans",Arial,sans-serif;color:var(--ink)}
.canvas{position:relative;width:1200px;height:552px}
.sheet{position:absolute;background:var(--paper);box-shadow:var(--shadow);overflow:hidden}
.fax-sheet{left:29px;top:24px;width:355px;height:499px}
.letter-sheet{left:403px;top:24px;width:355px;height:499px}
.brand-name{font-family:"Cormorant Garamond",Georgia,serif;font-weight:500;color:var(--brand);letter-spacing:.5px;line-height:1;white-space:nowrap}
.brand-mark{display:flex;align-items:center;gap:6px}
.brand-dot{width:10px;height:10px;border-radius:50%;background:var(--brand);flex:none}
.sheet .brand-mark{position:absolute;left:26px;top:22px}
.sheet .brand-name{font-size:26px}
.contact{position:absolute;right:18px;top:12px;font-size:4.6px;line-height:7px;color:var(--ink);width:110px}
.contact li{list-style:none;display:flex;gap:3px;align-items:center;white-space:nowrap}
.contact li::before{content:"";width:3px;height:3px;background:var(--ink);display:inline-block;flex:none}
.floral-fill{position:absolute;border-radius:50%;background:radial-gradient(circle,rgba(169,211,211,.35),rgba(169,211,211,0) 70%)}
.wave{position:absolute;left:0;bottom:0;width:100%;height:70px}
.fax-title{position:absolute;right:22px;top:88px;font-size:9px;font-weight:600;letter-spacing:1px}
.fax-table{position:absolute;left:20px;top:100px;width:315px;border-collapse:collapse;font-size:6px}
.fax-table td{border:1px solid var(--rule);height:17px;padding:0 5px}
.fax-table .label{width:45px}
.fax-options{position:absolute;left:20px;top:180px;width:315px;display:flex;justify-content:space-between;font-size:5.5px}
.fax-options span{display:flex;align-items:center;gap:3px}
.fax-options span::before{content:"";width:7px;height:7px;border:1px solid var(--rule)}
.card{position:absolute;top:24px;width:164px;height:89px;background:var(--night);border-radius:6px;color:#eee;overflow:hidden;box-shadow:var(--shadow)}
.card-front{left:773px}
.card-back{left:950px}
.card .brand-mark{position:absolute;left:12px;top:10px}
.card .brand-name{font-size:16px;color:#f2f2f2}
.card .brand-dot{width:7px;height:7px;background:var(--teal-deep)}
.card-front .contact{right:auto;left:12px;top:36px;color:#ddd;font-size:4.4px;line-height:6.6px;width:145px}
.card-front .contact li::before{background:var(--teal-deep)}
.card-tag{position:absolute;right:10px;top:15px;font-size:5px;color:var(--gold)}
.card .wave{height:24px}
.card-back .services{position:absolute;left:12px;top:32px;width:142px;font-size:4.4px;line-height:6.4px;color:#ddd}
.card-back .services li{list-style:none}
.card-back .services li::before{content:"• ";color:var(--gold)}
.envelope-front{left:775px;top:125px;width:396px;height:194px}
.envelope-front .brand-mark{left:24px;top:22px}
.envelope-back{left:775px;top:336px;width:396px;height:187px}
.flap{position:absolute;left:0;top:0;width:100%;height:140px}
.envelope-back .brand-mark{position:absolute;left:50%;top:62px;transform:translateX(-50%)}
.envelope-back .brand-name{color:#f2f2f2;font-size:18px}
.envelope-back .brand-dot{width:7px;height:7px;background:var(--teal-deep)}
</style>
</head>
<body>
<main class="canvas">

  <section class="sheet fax-sheet">
    <div class="brand-mark"><span class="brand-dot"></span><span class="brand-name">Saltmarsh</span></div>
    <ul class="contact">
      <li>#41 Estate Coralind</li>
      <li>(at the Harbor Bluff Cottages)</li>
      <li>Palmhaven, VI 00999</li>
      <li>Saltmarsh_Restaurant@bayvistamail.com</li>
      <li>www.saltmarshvi-example.com</li>
    </ul>
    <div class="fax-title">FAX</div>
    <table class="fax-table">
      <tr><td class="label">To:</td><td></td><td class="label">From:</td><td></td></tr>
      <tr><td class="label">Fax:</td><td></td><td class="label">Pages:</td><td></td></tr>
      <tr><td class="label">Phone:</td><td></td><td class="label">Date:</td><td></td></tr>
      <tr><td class="label">Re:</td><td></td><td class="label">CC:</td><td></td></tr>
    </table>
    <div class="fax-options"><span>Urgent</span><span>For Review</span><span>Please Comment</span><span>Please Reply</span><span>Please Recycle</span></div>
    <div class="floral-fill" role="img" aria-label="Faint floral decoration" style="left:150px;top:300px;width:200px;height:170px"></div>
    <svg class="wave" viewBox="0 0 355 70" preserveAspectRatio="none">
      <path d="M0 58 C90 40 200 52 355 26 L355 70 L0 70Z" fill="var(--teal)"/>
      <path d="M0 50 C100 30 210 46 355 18" fill="none" stroke="var(--gold)" stroke-width="1.4"/>
    </svg>
  </section>

  <section class="sheet letter-sheet">
    <div class="brand-mark"><span class="brand-dot"></span><span class="brand-name">Saltmarsh</span></div>
    <ul class="contact">
      <li>#41 Estate Coralind</li>
      <li>(at the Harbor Bluff Cottages)</li>
      <li>Palmhaven, VI 00999</li>
      <li>Saltmarsh_Restaurant@bayvistamail.com</li>
      <li>www.saltmarshvi-example.com</li>
    </ul>
    <div class="floral-fill" role="img" aria-label="Faint floral decoration" style="left:150px;top:300px;width:200px;height:170px"></div>
    <svg class="wave" viewBox="0 0 355 70" preserveAspectRatio="none">
      <path d="M0 58 C90 40 200 52 355 26 L355 70 L0 70Z" fill="var(--teal)"/>
      <path d="M0 50 C100 30 210 46 355 18" fill="none" stroke="var(--gold)" stroke-width="1.4"/>
    </svg>
  </section>

  <section class="card card-front">
    <div class="brand-mark"><span class="brand-dot"></span><span class="brand-name">Saltmarsh</span></div>
    <div class="card-tag">Truly Island-Made</div>
    <ul class="contact">
      <li>#41 Estate Coralind (at the Harbor Bluff Cottages)</li>
      <li>Palmhaven, VI 00999</li>
      <li>Saltmarsh_Restaurant@bayvistamail.com</li>
      <li>www.saltmarshvi-example.com</li>
    </ul>
    <svg class="wave" viewBox="0 0 164 24" preserveAspectRatio="none">
      <path d="M0 20 C50 14 100 18 164 8 L164 24 L0 24Z" fill="var(--teal-deep)"/>
      <path d="M0 16 C50 10 100 14 164 4" fill="none" stroke="var(--gold)" stroke-width="1"/>
    </svg>
  </section>

  <section class="card card-back">
    <div class="brand-mark"><span class="brand-dot"></span><span class="brand-name">Saltmarsh</span></div>
    <div class="card-tag">Truly Island-Made</div>
    <ul class="services">
      <li>Free Wi-fi</li>
      <li>Special events venue — meetings, fund raisers, wedding receptions, catering, private parties</li>
      <li>Superior customer service</li>
      <li>Delicious cuisine</li>
    </ul>
    <svg class="wave" viewBox="0 0 164 24" preserveAspectRatio="none">
      <path d="M0 20 C50 14 100 18 164 8 L164 24 L0 24Z" fill="var(--teal-deep)"/>
      <path d="M0 16 C50 10 100 14 164 4" fill="none" stroke="var(--gold)" stroke-width="1"/>
    </svg>
  </section>

  <section class="sheet envelope-front">
    <div class="brand-mark"><span class="brand-dot"></span><span class="brand-name" style="font-size:22px">Saltmarsh</span></div>
    <ul class="contact" style="right:auto;left:24px;top:54px">
      <li>#41 Estate Coralind</li>
      <li>(at the Harbor Bluff Cottages)</li>
      <li>Palmhaven, VI 00999</li>
      <li>www.saltmarshvi-example.com</li>
    </ul>
    <div class="floral-fill" role="img" aria-label="Faint floral decoration" style="left:160px;top:40px;width:200px;height:140px"></div>
    <svg class="wave" viewBox="0 0 396 50" preserveAspectRatio="none" style="height:50px">
      <path d="M0 42 C110 28 240 40 396 16 L396 50 L0 50Z" fill="var(--teal)"/>
      <path d="M0 36 C120 20 250 34 396 10" fill="none" stroke="var(--gold)" stroke-width="1.4"/>
    </svg>
  </section>

  <section class="sheet envelope-back">
    <svg class="flap" viewBox="0 0 396 140" preserveAspectRatio="none">
      <path d="M0 0 H396 V110 C300 100 250 140 198 140 C146 140 96 100 0 110Z" fill="var(--night)"/>
      <path d="M0 116 C96 106 146 132 198 132 C250 132 300 106 396 116" fill="none" stroke="var(--gold)" stroke-width="1"/>
    </svg>
    <div class="brand-mark"><span class="brand-dot"></span><span class="brand-name">Saltmarsh</span></div>
  </section>

</main>
</body>
</html>
```